New Web Design Project for kids music school

We need a homepage mockup for a kids' music program. Use your creative talent to come up with something visually appeal and professional for this web-site.

More information is provided in the PDF file called HOME. Also included in this file are links to the photos to be used.

Please let me know if you have more questions.

Target Market(s)

parents

Number of Pages Required

1 page

Font styles to use
Sans Serif

```html
<!DOCTYPE html>
<html lang="en">
<head>
<meta charset="utf-8">
<title>Little Notes – Kids Music Programs</title>
<link href="https://fonts.googleapis.com/css2?family=Arimo:wght@400;700&family=Raleway:wght@600;700&display=swap" rel="stylesheet">
<style>
:root{
  --blue:#6a9bc6;
  --footer:#6c9ecb;
  --ink:#2b2b2b;
  --text:#444;
  --white:#fff;
}
*{box-sizing:border-box;margin:0;padding:0}
html,body{width:1200px;height:3051px;overflow:hidden;background:var(--white)}
body{position:relative;font-family:"Arimo",Arial,sans-serif;color:var(--text)}

/* header */
.site-header{position:absolute;left:0;top:0;width:1200px;height:78px;background:var(--white)}
.brand{position:absolute;left:104px;top:22px;font:700 28px/1 "Arimo",sans-serif;color:#2f3db8}
.brand-dot{display:inline-block;width:12px;height:12px;border-radius:50%;background:#2f3db8;margin-left:6px;vertical-align:middle}
.main-nav{position:absolute;left:480px;top:30px;display:flex;gap:38px;font-size:20px;color:#111}
.main-nav .active{color:var(--blue)}
.header-phone{position:absolute;left:868px;top:29px;display:flex;align-items:center;gap:14px;color:var(--blue);font-size:21px;font-weight:700}

/* hero */
.hero{position:absolute;left:0;top:78px;width:1200px;height:553px;background:linear-gradient(100deg,#7f9a6a 0%,#b7c48f 45%,#c9cf98 70%,#8fa36d 100%)}
.hero-title{position:absolute;left:0;width:1200px;top:135px;text-align:center;font:700 44px/1 "Raleway",sans-serif;color:var(--white);text-shadow:0 2px 6px rgba(0,0,0,.55);letter-spacing:1px}
.hero-sub{position:absolute;left:0;width:1200px;top:190px;text-align:center;font-size:22px;line-height:36px;color:var(--white);text-shadow:0 1px 4px rgba(0,0,0,.6);white-space:nowrap}
.btn{position:absolute;left:515px;top:281px;width:172px;height:50px;border-radius:4px;background:var(--blue);color:var(--white);font:700 18px/50px "Raleway",sans-serif;text-align:center;letter-spacing:.5px}
.slider-dots{position:absolute;left:578px;top:530px;display:flex;gap:8px}
.slider-dots span{width:9px;height:9px;border-radius:50%;background:#111;border:1px solid #fff}
.slider-dots .on{background:var(--blue)}

/* program blocks */
.photo{position:absolute}
.photo-main{background:linear-gradient(135deg,#d8c08a,#b99a7a 50%,#8a7b70)}
.photo-inset{border:3px solid var(--white);box-shadow:0 2px 4px rgba(0,0,0,.15)}
.program-title{position:absolute;font-size:39px;font-weight:400;color:var(--blue);line-height:44px;letter-spacing:.5px}
.program-age{position:absolute;font:700 18px/1 "Raleway",sans-serif;color:#222}
.program-text{position:absolute;font-size:18px;line-height:35.3px;color:var(--text);letter-spacing:.5px;white-space:nowrap}

/* videos */
.videos{position:absolute;left:0;top:1172px;width:1200px;height:434px;background:linear-gradient(90deg,#d9d43a,#e3df4a 50%,#d6d23a)}
.videos h2{position:absolute;left:0;width:1200px;top:64px;text-align:center;font-weight:400;font-size:39px;color:#2a2a1a}
.video{position:absolute;top:160px;width:311px;height:217px;border:2px solid var(--white);background:linear-gradient(160deg,#c8b27e,#8e6f52 60%,#4b3b36)}
.play{position:absolute;left:50%;top:50%;width:48px;height:48px;margin:-30px 0 0 -24px;border-radius:50%;background:rgba(255,255,255,.85)}
.play:after{content:"";position:absolute;left:18px;top:13px;border-left:17px solid var(--blue);border-top:11px solid transparent;border-bottom:11px solid transparent}
.video-bar{position:absolute;left:0;right:0;bottom:0;height:14px;background:rgba(0,0,0,.55)}
.vdots{position:absolute;left:1114px;top:230px;display:flex;flex-direction:column;gap:14px}
.vdots span{width:9px;height:9px;border-radius:50%;background:var(--white)}

.divider{position:absolute;left:95px;top:2191px;width:1010px;height:1px;background:var(--blue)}

/* footer */
.site-footer{position:absolute;left:0;top:2685px;width:1200px;height:366px;background:linear-gradient(90deg,#6a9dcb,#74a4cf 50%,#6a9bc9);color:var(--white)}
.footer-brand{position:absolute;left:103px;top:56px;font:700 30px/1 "Arimo",sans-serif;color:var(--white)}
.footer-about{position:absolute;left:113px;top:140px;width:290px;font-size:16px;line-height:28px;letter-spacing:1.5px}
.footer-head{position:absolute;top:62px;font-size:20px;font-weight:400;padding-bottom:10px;border-bottom:1px solid var(--white)}
.contact-list{position:absolute;left:464px;top:134px;list-style:none;font-size:15px;line-height:27px}
.contact-list li{position:relative;padding-left:44px}
.contact-list svg{position:absolute;left:0;top:4px}
.socials{position:absolute;left:803px;top:139px;display:flex;gap:10px}
.socials span{width:28px;height:28px;border-radius:50%;border:2px solid var(--white)}
.legal{position:absolute;left:108px;top:328px;font-size:12px}
</style>
</head>
<body>

<header class="site-header">
  <div class="brand">Little Notes<span class="brand-dot"></span></div>
  <nav class="main-nav"><span class="active">Home</span><span>Programs</span><span>Contact Us</span></nav>
  <div class="header-phone">
    <svg width="20" height="22" viewBox="0 0 20 22"><path d="M4 1l4 5-2 3c1 3 4 6 7 7l3-2 4 4-3 3C9 21-1 11 2 3z" fill="#6a9bc6"/></svg>
    +1 (555) 201-4870
  </div>
</header>

<section class="hero" role="img" aria-label="Young children dancing with raised arms in a bright music classroom">
  <h1 class="hero-title">LITTLE NOTES</h1>
  <p class="hero-sub">Neque porro quisquam est qui dolorem ipsum quia dolor<br>sit amet, consectetur.</p>
  <div class="btn">GET STARTED</div>
  <div class="slider-dots"><span></span><span class="on"></span><span></span></div>
</section>

<!-- live music program -->
<div class="photo photo-main" style="left:111px;top:715px;width:396px;height:351px" role="img" aria-label="Toddlers exploring instruments together in class"></div>
<div class="photo photo-inset" style="left:309px;top:844px;width:247px;height:220px;background:linear-gradient(135deg,#9aa8c4,#7f8aa6)" role="img" aria-label="Toddler playing with a small wooden instrument"></div>
<h2 class="program-title" style="left:620px;top:708px">Live Music Program</h2>
<div class="program-age" style="left:625px;top:766px">3 Mos- 3 yrs.</div>
<p class="program-text" style="left:623px;top:799px">This “mommy &amp; me” style class is a 45 minute live<br>music adventure. Each class has a singer and<br>pianist guiding little ones through 3 boxes of<br>instruments built for their little hands. We use music<br>to teach movement, vocabulary, numbers,&nbsp; letters,<br>confidence and build a love of music.</p>

<section class="videos" role="img" aria-label="Blurred yellow-tinted photo of a teacher with children">
  <h2>Our Latest StreamBox Videos</h2>
  <div class="video" style="left:111px" role="img" aria-label="Video thumbnail of a teacher singing in the classroom"><span class="play"></span><span class="video-bar"></span></div>
  <div class="video" style="left:444px" role="img" aria-label="Video thumbnail of a teacher holding an instrument box"><span class="play"></span><span class="video-bar"></span></div>
  <div class="video" style="left:775px" role="img" aria-label="Video thumbnail of a teacher reading a storybook"><span class="play"></span><span class="video-bar"></span></div>
  <div class="vdots"><span></span><span></span><span></span></div>
</section>

<!-- sparks program -->
<h2 class="program-title" style="left:145px;top:1705px">SPARKS! Performance<br>Program</h2>
<div class="program-age" style="left:140px;top:1833px">3 - 14 yrs.</div>
<p class="program-text" style="left:140px;top:1867px">Kids work once a week to put on a show customized<br>for their class. Every child has a solo, lines, and a<br>big part. We have classes for kids ages 3-14. Our<br>mission is confidence and teaching important life<br>skills through theater. All classes perform their show<br>at the end of the session.</p>
<div class="photo photo-main" style="left:675px;top:1723px;width:396px;height:351px;background:linear-gradient(135deg,#d6bf8f,#a98a7a 50%,#5e6a7a)" role="img" aria-label="Group of children seated on the floor in a performance class"></div>
<div class="photo photo-inset" style="left:625px;top:1852px;width:247px;height:220px;background:linear-gradient(135deg,#c23a44,#3b6a46 60%,#2a2a2a)" role="img" aria-label="Children in holiday costumes on stage"></div>

<div class="divider"></div>

<!-- virtual lessons -->
<div class="photo photo-main" style="left:111px;top:2270px;width:396px;height:351px;background:linear-gradient(135deg,#aebc88,#8b9a72 50%,#6f7286)" role="img" aria-label="Children dancing in a green classroom"></div>
<div class="photo photo-inset" style="left:309px;top:2399px;width:247px;height:220px;background:linear-gradient(135deg,#7ea04e,#d9a2b8 60%,#5a6ea0)" role="img" aria-label="Smiling toddlers sitting and waving"></div>
<h2 class="program-title" style="left:627px;top:2266px">Virtual Music Lessons</h2>
<div class="program-age" style="left:630px;top:2335px">3 Mos- 3 yrs.</div>
<p class="program-text" style="left:631px;top:2370px">Lorem ipsum dolor sit amet, consectetur adipiscing<br>elit, sed do eiusmod tempor incididunt ut labore et<br>dolore magna aliqua. Ut enim ad minim veniam,<br>quis nostrud exercitation ullamco laboris nisi ut<br>aliquip ex ea commodo consequat.Duis aute irure<br>dolor in reprehenderit in voluptate.</p>

<footer class="site-footer">
  <div class="footer-brand">Little Notes</div>
  <p class="footer-about">Neque porro quisquam est qui<br>dolorem ipsum quia dolor sit<br>amet, consectetur.</p>
  <h3 class="footer-head" style="left:460px">QUICK LINKS</h3>
  <ul class="contact-list">
    <li><svg width="16" height="22" viewBox="0 0 16 22"><path d="M8 0a8 8 0 0 1 8 8c0 6-8 14-8 14S0 14 0 8a8 8 0 0 1 8-8z" fill="#fff"/><circle cx="8" cy="8" r="3" fill="#6c9ecb"/></svg>14 Maple Grove Rd. Fairview,<br>MA 01999</li>
    <li style="margin-top:16px"><svg width="18" height="18" viewBox="0 0 20 22"><path d="M4 1l4 5-2 3c1 3 4 6 7 7l3-2 4 4-3 3C9 21-1 11 2 3z" fill="#fff"/></svg>Tel: (555) 201-4870</li>
    <li style="margin-top:18px"><svg width="20" height="15" viewBox="0 0 20 15"><rect width="20" height="15" rx="1" fill="#fff"/><path d="M0 1l10 7 10-7" stroke="#6c9ecb" stroke-width="1.5" fill="none"/></svg>Email: hello@littlenotesmusic.com</li>
  </ul>
  <h3 class="footer-head" style="left:803px">FLLOW US</h3>
  <div class="socials"><span></span><span></span><span></span><span></span><span></span><span></span></div>
  <div class="legal">© 2020 All Rights Reserved | Privacy Policy | Terms and Conditions | Impressum</div>
</footer>

</body>
</html>
```